Bref créative
Corvale Power Associates, LLC
Stationery and business cards
Professional
Dean Halvorsen
President
28715 Birchwood Crest Lane
Suite 615
Marlow Springs, TX 77512
dean.halvorsen@corvale-pa.com
We will need multiple name, cell phone, and email changes. Primary colors should be white, black, and a vibrant blue.
Here is our logo Ai.

```html
<!DOCTYPE html>
<html lang="en">
<head>
<meta charset="utf-8">
<title>Corvale Power Associates — Stationery</title>
<link rel="stylesheet" href="https://fonts.googleapis.com/css2?family=Arimo:wght@400;700&display=swap">
<style>
  :root {
    --page-bg: #ffffff;
    --frame: #e3e3e3;
    --paper: #ffffff;
    --paper-edge: #d6d6d6;
    --ink: #1a1a1a;
    --blue-deep: #0a4fa8;
    --blue-bright: #1d8fe0;
    --flap-line: #9a9a9a;
  }
  * { margin: 0; padding: 0; box-sizing: border-box; }
  html, body { width: 1200px; height: 681px; overflow: hidden; background: var(--page-bg); }
  body { font-family: "Arimo", Arial, sans-serif; color: var(--ink); position: relative; }

  .presentation-frame {
    position: absolute; left: 12px; top: 12px; width: 1176px; height: 637px;
    border: 1px solid var(--frame);
  }
  .sheet {
    position: absolute; background: var(--paper); border: 1px solid var(--paper-edge); overflow: hidden;
  }
  .top-band { position: absolute; left: 0; top: 0; width: 100%; background: var(--blue-bright); }
  .top-band::after {
    content: ""; position: absolute; left: 0; right: 0; bottom: -3px; height: 1px; background: var(--blue-deep);
  }

  .brand-block { position: absolute; display: flex; align-items: center; }
  .brand { display: flex; align-items: center; gap: 5px; white-space: nowrap; }
  .brand-dot { border-radius: 50%; background: var(--blue-bright); flex: none; }
  .brand-name { font-weight: 700; color: var(--blue-deep); letter-spacing: 0.02em; }
  .divider { background: var(--ink); flex: none; width: 1px; }
  .contact { color: var(--ink); line-height: 1.4; white-space: nowrap; }
  .contact .person { font-weight: 700; color: var(--blue-deep); }
  .contact .role { display: block; margin-bottom: 4px; }

  /* Envelope front */
  .envelope-front { left: 60px; top: 96px; width: 324px; height: 156px; }
  .envelope-front .top-band { height: 6px; }
  .envelope-front .brand-block { left: 16px; top: 26px; }
  .envelope-front .brand-dot { width: 9px; height: 9px; }
  .envelope-front .brand-name { font-size: 13px; }
  .envelope-front .divider { height: 36px; margin: 0 8px; }
  .envelope-front .contact { font-size: 5.5px; }

  /* Envelope back */
  .envelope-back { left: 60px; top: 283px; width: 324px; height: 161px; }
  .envelope-back .flap { position: absolute; left: 0; top: 0; }
  .envelope-back .seal-mark {
    position: absolute; left: 152px; top: 92px; width: 20px; height: 20px;
    border-radius: 50%; background: var(--blue-bright);
  }

  /* Letterhead */
  .letterhead { left: 619px; top: 43px; width: 312px; height: 576px; }
  .letterhead .top-band { height: 8px; }
  .letterhead .brand-block { left: 16px; top: 40px; }
  .letterhead .brand-dot { width: 10px; height: 10px; }
  .letterhead .brand-name { font-size: 15px; }
  .letterhead .divider { height: 46px; margin: 0 9px; }
  .letterhead .contact { font-size: 6px; }

  /* Business card */
  .card-front { left: 967px; top: 182px; width: 173px; height: 101px; }
  .card-front .top-band { height: 4px; }
  .card-front .brand-block { left: 10px; top: 24px; }
  .card-front .brand-dot { width: 7px; height: 7px; }
  .card-front .brand-name { font-size: 10px; }
  .card-front .divider { height: 56px; margin: 0 6px; }
  .card-front .contact { font-size: 4.6px; }
  .card-back { left: 967px; top: 312px; width: 173px; height: 101px; }
  .card-back .seal-mark {
    position: absolute; left: 76px; top: 40px; width: 20px; height: 20px;
    border-radius: 50%; background: var(--blue-bright);
  }
</style>
</head>
<body>
<div class="presentation-frame"></div>

<section class="sheet envelope-front" aria-label="Envelope front">
  <span class="top-band"></span>
  <div class="brand-block">
    <div class="brand"><span class="brand-dot"></span><span class="brand-name">Corvale</span></div>
    <span class="divider"></span>
    <div class="contact">
      28715 Birchwood Crest Lane<br>
      Suite 615<br>
      Marlow Springs, TX 77512<br>
      dean.halvorsen@corvale-pa.com
    </div>
  </div>
</section>

<section class="sheet envelope-back" aria-label="Envelope back">
  <svg class="flap" width="324" height="161" viewBox="0 0 324 161">
    <path d="M4 6 C40 40 100 62 162 64 C224 62 284 40 320 6" fill="none" stroke="var(--flap-line)" stroke-width="1"/>
  </svg>
  <span class="seal-mark"></span>
</section>

<section class="sheet letterhead" aria-label="Letterhead">
  <span class="top-band"></span>
  <div class="brand-block">
    <div class="brand"><span class="brand-dot"></span><span class="brand-name">Corvale</span></div>
    <span class="divider"></span>
    <div class="contact">
      28715 Birchwood Crest Lane<br>
      Suite 615<br>
      Marlow Springs, TX 77512<br>
      Phone: (281) 555-0139<br>
      dean.halvorsen@corvale-pa.com
    </div>
  </div>
</section>

<section class="sheet card-front" aria-label="Business card front">
  <span class="top-band"></span>
  <div class="brand-block">
    <div class="brand"><span class="brand-dot"></span><span class="brand-name">Corvale</span></div>
    <span class="divider"></span>
    <div class="contact">
      <span class="person">Dean Halvorsen</span><br>
      <span class="role">President</span>
      28715 Birchwood Crest Lane<br>
      Suite 615<br>
      Marlow Springs, TX 77512<br>
      Phone: (281) 555-0139<br>
      dean.halvorsen@corvale-pa.com
    </div>
  </div>
</section>

<section class="sheet card-back" aria-label="Business card back">
  <span class="seal-mark"></span>
</section>
</body>
</html>
```